Startup Biz for Seniors needs your help!

Our business is a Startup that Employs Caregivers to do IN HOME Care of the Elderly. Our website is not yet running. But, a business similar to ours is Tallbrookcare.com

We are looking for a card that only has 4 Elements:
-Logo
- Website
- Tag Line
- Phone
We would like to see some eye catching backgrounds.
We would like to see some designs with and some without a Photo.
Would like the Photo to be of a Caregiver taking care of a Senior. The photo should show both of them smiling.

Target Market(s)

Age 35-55 who has Parents that are Elderly and need care

Industry/Entity Type

Home Health Care

Contact Information for Business Card

Want it to Pop Out to the viewer . Thinking maybe:
Side 1: LOGO with Website & Tag line
Side 2: Phone Number

Font styles to use
Other font styles liked:
• Same Font as our Logo

Colors

Designer to choose colors to be used in the design.

Requirements
Must have
• Logo, website, Tag Line, Phone number and Email: "info@velvetdays.example"
• Please use one of the photos that I have attached.
Nice to have
• Would like to see a Photo worked in that has a Care Taker taking care of an Elderly Person and they are both smiling.

```html
<!DOCTYPE html>
<html lang="en">
<head>
<meta charset="utf-8">
<title>VelvetDays.example – Business Card</title>
<link rel="stylesheet" href="https://fonts.googleapis.com/css2?family=Courgette&family=Roboto+Condensed:wght@400&display=swap">
<style>
  :root {
    --brand-blue: #1c5aa8;
    --brand-orange: #e8731c;
    --text-grey: #77787a;
    --card-white: #fbfbfb;
    --stage: #e9e7e4;
    --photo-light: #e4d6c6;
    --photo-dark: #8d8a86;
  }
  * { box-sizing: border-box; margin: 0; padding: 0; }
  html, body {
    width: 1200px; height: 866px; overflow: hidden;
    background: var(--stage);
  }
  .canvas { position: relative; width: 1200px; height: 866px; }

  .card {
    position: absolute;
    width: 580px; height: 332px;
    background: var(--card-white);
    border-radius: 4px;
    box-shadow: 0 10px 24px rgba(0,0,0,0.18);
    overflow: hidden;
  }

  /* Front side */
  .card--front { left: 60px; top: 70px; }
  .brand-lockup {
    position: absolute; left: 44px; top: 66px;
    display: flex; align-items: center; gap: 18px;
  }
  .brand-dot {
    width: 74px; height: 74px; border-radius: 50%;
    background: var(--brand-orange);
    flex: none;
  }
  .brand-text { display: flex; flex-direction: column; }
  .brand-name {
    font-family: "Courgette", cursive;
    font-size: 40px; line-height: 1;
    color: var(--brand-blue);
  }
  .tagline {
    font-family: "Courgette", cursive;
    font-size: 21px; margin-top: 8px;
    color: var(--brand-blue);
  }
  .contact {
    position: absolute; left: 0; right: 0; top: 190px;
    display: flex; flex-direction: column; align-items: center;
  }
  .contact-rule { display: flex; align-items: center; gap: 10px; }
  .contact-rule .line { width: 120px; height: 1.5px; background: var(--brand-blue); }
  .phone-icon {
    width: 26px; height: 26px; border-radius: 50%;
    background: var(--brand-blue);
    display: flex; align-items: center; justify-content: center;
  }
  .phone-number {
    font-family: "Roboto Condensed", sans-serif;
    font-size: 40px; line-height: 1.1; letter-spacing: 1px;
    color: var(--text-grey); margin-top: 8px;
  }
  .email {
    font-family: "Roboto Condensed", sans-serif;
    font-size: 19px; letter-spacing: 0.5px;
    color: var(--brand-blue); margin-top: 6px;
  }

  /* Back side */
  .card--back { left: 560px; top: 470px; }
  .photo {
    position: absolute; inset: 0;
    background: linear-gradient(160deg, var(--photo-dark) 0%, var(--photo-light) 55%, #f2ece6 100%);
  }
  .back-disc {
    position: absolute; left: -200px; top: -130px;
    width: 560px; height: 560px; border-radius: 50%;
    background: var(--card-white);
    border: 18px solid var(--brand-blue);
  }
  .back-brand {
    position: absolute; left: 0; top: 0; width: 320px; height: 100%;
    display: flex; flex-direction: column; align-items: center; justify-content: center;
    gap: 16px; padding-right: 20px;
  }
  .back-brand .brand-dot { width: 120px; height: 120px; }
  .back-brand .brand-name { font-size: 25px; }
  .web-pill {
    position: absolute; right: 0; bottom: 40px;
    background: #ffffff;
    border-radius: 28px 0 0 28px;
    padding: 10px 22px 10px 26px;
    font-family: "Courgette", cursive;
    font-size: 22px; color: var(--brand-blue);
  }
</style>
</head>
<body>
<main class="canvas">
  <section class="card card--front" aria-label="Card front">
    <div class="brand-lockup">
      <span class="brand-dot"></span>
      <div class="brand-text">
        <span class="brand-name">VelvetDays.example</span>
        <span class="tagline">Senior Care – Family Style</span>
      </div>
    </div>
    <div class="contact">
      <div class="contact-rule">
        <span class="line"></span>
        <span class="phone-icon">
          <svg width="14" height="14" viewBox="0 0 24 24" aria-hidden="true">
            <path fill="#fff" d="M6.6 10.8a15.1 15.1 0 0 0 6.6 6.6l2.2-2.2c.3-.3.7-.4 1-.2 1.1.4 2.3.6 3.6.6.6 0 1 .4 1 1V20c0 .6-.4 1-1 1A17 17 0 0 1 3 4c0-.6.4-1 1-1h3.5c.6 0 1 .4 1 1 0 1.3.2 2.5.6 3.6.1.3 0 .7-.2 1z"/>
          </svg>
        </span>
        <span class="line"></span>
      </div>
      <span class="phone-number">(555) 014-2290</span>
      <span class="email">info@velvetdays.example</span>
    </div>
  </section>

  <section class="card card--back" aria-label="Card back">
    <div class="photo" role="img" aria-label="Photo of a smiling caregiver with her hand on the shoulder of a smiling senior woman"></div>
    <div class="back-disc"></div>
    <div class="back-brand">
      <span class="brand-dot"></span>
      <span class="brand-name">VelvetDays.example</span>
    </div>
    <span class="web-pill">VelvetDays.example</span>
  </section>
</main>
</body>
</html>
```